Business card design needed

We are a company that provides women with executive support. We organise a range of services including - transportation, relocation, home and office support and bespoke custom fit garments and anything to assist in their busy lifestyle.

The colours we would like are bright blue on the back and front is white with design. We have an example card that we would be happy to use. My son designed these cards but did not print well. Happy for you to use his design by tweaking it and adding a description of our service on the back of the card and making the back look easier to read . Also need the hotmail address and phone and abn. We will also need a website organised through pluma - are you able to add www.brightlaneassist.com.au to the card..?. Any questions pls contact me on 0417586293 Mara

Thank you
Updates

business card needed to start new business - please note sample of business card we are happy for you to use.

Industry/Entity Type

Business

Contact Information for Business Card

The brightlane crew
Let us organise you!

Executive support for women

brightlanecrew@maildrop-example.com
ph: Mara 0417 586 293 or Joan 0438 270 915
abn: 21604873519

```html
<!DOCTYPE html>
<html lang="en">
<head>
<meta charset="utf-8">
<title>The Brightlane Crew – Business Cards</title>
<link rel="stylesheet" href="https://fonts.googleapis.com/css2?family=Jost:wght@400;500;600&display=swap">
<style>
  :root {
    --backdrop: #f2f2f2;
    --front-panel: #e5e5e5;
    --front-bar-light: #b4b4b4;
    --front-bar-dark: #5b5b5b;
    --ink: #1a1a1a;
    --white: #ffffff;
    --brand-blue: #2c56a6;
    --grey-dark: #3a3a3a;
    --grey-mid: #8a8a8a;
    --grey-light: #c9c9c9;
  }
  * { box-sizing: border-box; margin: 0; padding: 0; }
  html, body { width: 1200px; height: 900px; overflow: hidden; }
  body {
    background: var(--backdrop);
    font-family: "Jost", "Futura", sans-serif;
    position: relative;
  }
  .card {
    position: absolute;
    top: 283px;
    width: 476px;
    height: 291px;
    overflow: hidden;
  }
  .card--front { left: 109px; background: var(--front-panel); }
  .card--back { left: 628px; background: var(--brand-blue); color: var(--white); }

  /* Front */
  .front-brand {
    position: absolute;
    left: 26px;
    top: 80px;
    font-weight: 500;
    font-size: 26px;
    line-height: 1.02;
    letter-spacing: 0.5px;
    color: var(--ink);
    text-transform: uppercase;
  }
  .front-artwork {
    position: absolute;
    left: 228px;
    top: 0;
    width: 248px;
    height: 261px;
    background: linear-gradient(135deg, var(--grey-mid) 0%, var(--grey-light) 35%, var(--grey-dark) 65%, var(--grey-mid) 100%);
  }
  .front-bar {
    position: absolute;
    bottom: 0;
    height: 30px;
    display: flex;
    align-items: center;
    justify-content: center;
    font-size: 13.5px;
    text-transform: uppercase;
    letter-spacing: 0.3px;
  }
  .front-bar--tagline { left: 0; width: 228px; background: var(--front-bar-light); color: var(--grey-dark); }
  .front-bar--service { left: 228px; width: 248px; background: var(--front-bar-dark); color: var(--white); }

  /* Back */
  .service-tab {
    position: absolute;
    left: 0;
    top: 69px;
    width: 252px;
    height: 26px;
    background: var(--white);
    color: var(--brand-blue);
    font-size: 13px;
    text-transform: uppercase;
    display: flex;
    align-items: center;
    padding-left: 18px;
    letter-spacing: 0.2px;
  }
  .back-brand {
    position: absolute;
    left: 282px;
    top: 36px;
    font-weight: 500;
    font-size: 25px;
    line-height: 1.02;
    letter-spacing: 0.5px;
    text-transform: uppercase;
  }
  .back-tagline {
    position: absolute;
    left: 282px;
    top: 140px;
    font-size: 17px;
    font-weight: 500;
  }
  .contacts {
    position: absolute;
    right: 224px;
    top: 165px;
    text-align: right;
    font-size: 14px;
    line-height: 18px;
  }
  .link-row {
    position: absolute;
    left: 18px;
    display: flex;
    align-items: center;
    gap: 10px;
    font-size: 13px;
  }
  .link-row--email { top: 222px; }
  .link-row--web { top: 251px; }
  .link-row svg { width: 22px; height: 22px; flex: none; }
  .abn {
    position: absolute;
    right: 34px;
    top: 258px;
    font-size: 11.5px;
  }
</style>
</head>
<body>
  <section class="card card--front" aria-label="Business card front">
    <div class="front-brand">The<br>Brightlane<br>Crew</div>
    <div class="front-artwork" role="img" aria-label="Geometric triangle pattern in greys with one red and two blue triangles"></div>
    <div class="front-bar front-bar--tagline">Let us organise you</div>
    <div class="front-bar front-bar--service">Executive support for women</div>
  </section>

  <section class="card card--back" aria-label="Business card back">
    <div class="service-tab">Executive support for women</div>
    <div class="back-brand">The<br>Brightlane<br>Crew</div>
    <div class="back-tagline">Let us organise you!</div>
    <div class="contacts">
      <p>Mara 0417 586 293</p>
      <p>Joan 0438 270 915</p>
    </div>
    <div class="link-row link-row--email">
      <svg viewBox="0 0 24 24" aria-hidden="true">
        <rect x="2" y="6" width="20" height="14" rx="1.5" fill="#fff"/>
        <path d="M3 7 L12 14 L21 7" fill="none" stroke="#2c56a6" stroke-width="1.6"/>
      </svg>
      <span>brightlanecrew@maildrop-example.com</span>
    </div>
    <div class="link-row link-row--web">
      <svg viewBox="0 0 24 24" aria-hidden="true">
        <circle cx="12" cy="12" r="10" fill="#fff"/>
        <g fill="none" stroke="#2c56a6" stroke-width="1.3">
          <ellipse cx="12" cy="12" rx="4.5" ry="10"/>
          <line x1="2" y1="12" x2="22" y2="12"/>
          <line x1="12" y1="2" x2="12" y2="22"/>
        </g>
      </svg>
      <span>www.brightlaneassist.com.au</span>
    </div>
    <div class="abn">abn: 21604873519</div>
  </section>
</body>
</html>
```